TORVEN RENEWABLES

New business B2B Energy Renewables website.
Please refer to our competitor https://www.quorbit72.co.uk/ for a similar website.

Need extra days to review

```html
<!DOCTYPE html>
<html lang="en">
<head>
<meta charset="utf-8">
<title>Torven Renewables</title>
<link rel="stylesheet" href="https://fonts.googleapis.com/css2?family=Montserrat:wght@500;600;700&family=Lato:wght@400;700&family=Poppins:wght@400;500&display=swap">
<style>
:root{
  --blue:#3a6cb0;
  --navy:#1c3d6e;
  --ink:#333333;
  --text:#444444;
  --field:#efefef;
  --footer:#333333;
  --white:#ffffff;
}
*{box-sizing:border-box;margin:0;padding:0}
html,body{width:1200px;height:3624px;overflow:hidden;background:var(--white)}
body{position:relative;font-family:'Lato',sans-serif;color:var(--text)}
.abs{position:absolute}
.heading{font-family:'Montserrat',sans-serif;font-weight:600;color:var(--ink);text-align:center;letter-spacing:.5px}

/* header */
.brand{left:75px;top:40px;font-family:'Montserrat',sans-serif;font-weight:700;font-size:20px;color:var(--navy);letter-spacing:2px;display:flex;align-items:center;gap:10px}
.brand i{display:block;width:26px;height:26px;background:var(--blue)}
.nav{top:52px;font-family:'Poppins',sans-serif;font-size:13px;color:#333;transform:translateX(-50%);white-space:nowrap}
.nav.active{font-weight:500;color:var(--navy)}
.nav.active::after{content:"";position:absolute;left:0;right:0;bottom:-7px;height:2px;background:var(--navy)}

/* hero */
.hero{left:0;top:117px;width:1200px;height:640px;background:linear-gradient(180deg,#6b9fd3 0%,#a9c8e4 38%,#8b99a4 50%,#7c8f86 62%,#c3ccd3 85%,#e3e8ec 100%)}
.hero-title{left:0;width:1200px;top:362px;text-align:center;color:var(--white);font-family:'Montserrat',sans-serif;font-weight:700;font-size:74px;letter-spacing:2px;line-height:1}
.hero-sub{left:0;width:1200px;top:446px;text-align:center;color:var(--white);font-family:'Montserrat',sans-serif;font-weight:600;font-size:33px;line-height:1}
.dot{left:1160px;width:7px;height:7px;border-radius:50%;background:rgba(255,255,255,.85)}

/* about */
.about-img{left:114px;top:937px;width:460px;height:308px;border-radius:20px;background:linear-gradient(180deg,#cfe0ef 0%,#e8eef3 45%,#4866a0 60%,#2f4b85 80%,#6e8a5a 100%)}
.about-text{left:623px;top:934px;width:465px;font-size:13px;line-height:21px;color:#444}
.about-text p{margin-bottom:21px}
.btn{display:flex;align-items:center;justify-content:center;background:var(--blue);color:var(--white);border-radius:22px;font-family:'Poppins',sans-serif}
.underline{height:4px;background:var(--blue)}

/* service */
.service{left:0;top:1345px;width:1200px;height:687px;background:var(--blue)}
.svc-title{top:1415px;left:0;width:1200px;font-family:'Montserrat',sans-serif;font-weight:600;font-size:33px;color:var(--white);text-align:center}
.svc-house{left:347px;top:1470px;width:466px;height:364px;border-radius:50%;background:radial-gradient(circle at 50% 40%,#e9eef4 0%,#b8c9de 40%,#6d8fbf 75%,#4a75b3 100%)}
.svc-item{color:var(--white)}
.svc-item h3{font-family:'Montserrat',sans-serif;font-weight:600;font-size:17px;letter-spacing:.5px;display:flex;align-items:center;gap:10px}
.svc-item p{font-size:13px;line-height:22px;margin-top:10px}
.svc-item .arrow{margin-top:8px;display:block}
.svc-left{text-align:right}
.svc-left h3{justify-content:flex-end}

/* solutions */
.card{top:2223px;width:326px;height:310px;border-radius:28px;overflow:hidden}
.card span{position:absolute;left:0;right:0;bottom:22px;text-align:center;color:var(--white);font-family:'Montserrat',sans-serif;font-weight:600;font-size:17px;line-height:21px}

/* contact */
.field{background:var(--field);font-family:'Poppins',sans-serif;font-style:italic;font-size:12px;color:#555;padding:12px 18px}

/* footer */
.footer{left:0;top:3207px;width:1200px;height:356px;background:var(--footer)}
.foot-title{font-family:'Poppins',sans-serif;font-size:14px;color:var(--white)}
.foot-title::after{content:"";display:block;width:38px;height:1px;background:var(--white);margin-top:10px}
.foot-txt{font-family:'Poppins',sans-serif;font-size:13px;color:var(--white);line-height:27px}
.links{list-style:none;font-family:'Poppins',sans-serif;font-size:12px;color:var(--white);line-height:27px}
.links li::before{content:"›";margin-right:12px}
.social{top:3580px;width:30px;height:30px;border-radius:50%}
</style>
</head>
<body>

<!-- header -->
<div class="abs brand"><i></i>TORVEN RENEWABLES</div>
<div class="abs nav active" style="left:602px">Home</div>
<div class="abs nav" style="left:691px">About us</div>
<div class="abs nav" style="left:798px">Our Services</div>
<div class="abs nav" style="left:946px">Renewable Solutions</div>
<div class="abs nav" style="left:1089px">Contact us</div>

<!-- hero -->
<div class="abs hero" role="img" aria-label="City skyline behind rows of solar panels in a field"></div>
<svg class="abs" style="left:0;top:640px" width="1200" height="125" viewBox="0 0 1200 125">
  <path d="M0 40 Q600 160 1200 40 L1200 125 L0 125 Z" fill="#ffffff"/>
  <path d="M0 42 Q150 95 390 112" stroke="#0e2740" stroke-width="7" fill="none"/>
  <path d="M830 112 Q1050 95 1200 42" stroke="#3a6cb0" stroke-width="7" fill="none"/>
  <circle cx="600" cy="114" r="14" fill="#ffffff"/>
  <path d="M596 112 L600 116 L604 112" stroke="#333" stroke-width="1.2" fill="none"/>
</svg>
<div class="abs hero-title">RENEWABLES</div>
<div class="abs hero-sub">ENERGY SAVING MONITORING</div>
<div class="abs dot" style="top:388px"></div>
<div class="abs dot" style="top:405px"></div>
<div class="abs dot" style="top:423px;opacity:.5"></div>

<!-- about -->
<div class="abs heading" style="left:0;width:1200px;top:838px;font-size:32px">ABOUT US</div>
<div class="abs underline" style="left:564px;top:890px;width:72px"></div>
<div class="abs about-img" role="img" aria-label="Engineer with clipboard standing beside solar panels"></div>
<div class="abs about-text">
  <p>Quorbit-72 aims to be a leading player in the UK's energy transformation agenda.</p>
  <p>To fulfil this ambitious vision, we have partnered with ethical organisations with a proven track record and a genuine commitment to changing the way we address energy generation, storage, management, distribution, carbon reduction and, importantly, project finance with ethical green funding institutions</p>
  <p>We are working with both private and public sector organisations to help reduce energy consumption, save money, and cut carbon emissions, to help meet the UK Government 2050 carbon targets.</p>
</div>
<div class="abs btn" style="left:622px;top:1204px;width:153px;height:40px;font-size:13px">Read More</div>

<!-- service -->
<div class="abs service"></div>
<div class="abs svc-title">OUR SERVICE</div>
<svg class="abs" style="left:340px;top:1400px" width="480" height="520" viewBox="0 0 480 520">
  <circle cx="240" cy="253" r="236" fill="none" stroke="rgba(255,255,255,.3)" stroke-dasharray="4 5"/>
</svg>
<div class="abs svc-house" role="img" aria-label="Modern house with solar panel roof"></div>

<div class="abs svc-item svc-left" style="left:60px;top:1520px;width:254px">
  <h3>CONSULTING <svg width="34" height="34" viewBox="0 0 34 34"><circle cx="20" cy="12" r="9" fill="none" stroke="#fff" stroke-width="3"/><path d="M4 26 H18 L28 22" stroke="#fff" stroke-width="3" fill="none"/></svg></h3>
  <p>Lorem Ipsum is simply dummy text of theprinting and typesetting industry</p>
  <svg class="arrow" style="margin-left:auto" width="30" height="10"><path d="M29 5 H2 M7 1 L2 5 L7 9" stroke="#fff" stroke-width="1.5" fill="none"/></svg>
</div>
<div class="abs svc-item svc-left" style="left:60px;top:1676px;width:260px">
  <h3>INSTALLATION <svg width="56" height="40" viewBox="0 0 56 40"><circle cx="18" cy="14" r="8" fill="#fff"/><path d="M14 34 L24 18 H54 L46 34 Z" fill="none" stroke="#fff" stroke-width="2.5"/></svg></h3>
  <p>Lorem Ipsum is simply dummy text of theprinting and typesetting industry</p>
  <svg class="arrow" style="margin-left:auto;margin-right:6px" width="30" height="10"><path d="M29 5 H2 M7 1 L2 5 L7 9" stroke="#fff" stroke-width="1.5" fill="none"/></svg>
</div>
<div class="abs svc-item" style="left:843px;top:1518px;width:260px">
  <h3><svg width="44" height="46" viewBox="0 0 44 46"><rect x="6" y="4" width="18" height="22" fill="none" stroke="#fff" stroke-width="2.5"/><circle cx="30" cy="34" r="9" fill="#fff"/></svg>FINANCE</h3>
  <p style="margin-left:19px">Lorem Ipsum is simply dummy text of the printing and typesetting industry</p>
  <svg class="arrow" style="margin-left:19px" width="30" height="10"><path d="M1 5 H28 M23 1 L28 5 L23 9" stroke="#fff" stroke-width="1.5" fill="none"/></svg>
</div>
<div class="abs svc-item" style="left:855px;top:1672px;width:250px">
  <h3><svg width="46" height="44" viewBox="0 0 46 44"><circle cx="22" cy="22" r="15" fill="none" stroke="#fff" stroke-width="6" stroke-dasharray="7 4"/><circle cx="22" cy="22" r="6" fill="#fff"/></svg>MAINTENANCE</h3>
  <p style="margin-left:7px">Lorem Ipsum is simply dummy text of the printing and typesetting industry</p>
  <svg class="arrow" style="margin-left:7px" width="30" height="10"><path d="M1 5 H28 M23 1 L28 5 L23 9" stroke="#fff" stroke-width="1.5" fill="none"/></svg>
</div>
<div class="abs svc-item" style="left:460px;top:1856px;width:280px;text-align:center">
  <h3 style="justify-content:center"><svg width="40" height="40" viewBox="0 0 40 40"><path d="M6 34 L30 6 L36 12 L12 38 Z" fill="#fff"/><path d="M4 8 L34 34" stroke="#fff" stroke-width="5"/></svg>DESIGN</h3>
  <p>Lorem Ipsum is simply dummy text of the printing and typesetting industry</p>
  <svg class="arrow" style="margin:6px auto 0" width="30" height="10"><path d="M1 5 H28 M23 1 L28 5 L23 9" stroke="#fff" stroke-width="1.5" fill="none"/></svg>
</div>

<!-- solutions -->
<div class="abs heading" style="left:0;width:1220px;top:2132px;font-size:33px">RENEWABLE SOLUTIONS</div>
<div class="abs card" style="left:75px;background:linear-gradient(160deg,#d8e6f3 0%,#5a86b8 40%,#2c5a92 70%,#4d6b52 100%)" role="img" aria-label="Wind turbines above solar panels by a lake"><span>VARIOUS RENEWABLES<br>OFFERED</span></div>
<div class="abs card" style="left:436px;background:radial-gradient(circle at 50% 45%,#c8a86a 0%,#6b5a34 45%,#2d3322 100%)" role="img" aria-label="Hands holding a glowing light bulb surrounded by eco icons"><span>ENERGY SAVING<br>ASSESSMENT</span></div>
<div class="abs card" style="left:799px;background:linear-gradient(180deg,#8a4d3a 0%,#2a4f92 35%,#1f3f7a 60%,#d3a88a 100%)" role="img" aria-label="Hands using a tablet with a home control app"><span>MONITORING</span></div>

<!-- contact -->
<div class="abs" style="left:114px;top:2732px;font-family:'Montserrat',sans-serif;font-weight:600;font-size:35px;color:var(--ink);letter-spacing:1px">CONTACTS US</div>
<div class="abs" style="left:114px;top:2779px;width:82px;height:4px;background:#eaeaea"></div>
<div class="abs field" style="left:114px;top:2804px;width:238px;height:42px">Full Name*</div>
<div class="abs field" style="left:364px;top:2804px;width:238px;height:42px">Email*</div>
<div class="abs field" style="left:114px;top:2858px;width:238px;height:42px">Phone*</div>
<div class="abs field" style="left:364px;top:2858px;width:238px;height:42px">City<span style="position:absolute;right:10px;font-style:normal">˅</span></div>
<div class="abs field" style="left:114px;top:2912px;width:488px;height:78px">Message</div>
<div class="abs btn" style="left:114px;top:3007px;width:188px;height:42px;font-size:13px">SEND</div>
<div class="abs" style="left:684px;top:2631px;width:406px;height:507px;border-radius:50% 50% 50% 50% / 30% 30% 70% 70%;background:radial-gradient(circle at 50% 70%,#e6edf5 0%,#a9c1de 45%,#2d6bb3 80%,#f2f5f9 100%)" role="img" aria-label="Half globe topped with a city skyline, wind turbines and solar panels"></div>

<!-- footer -->
<div class="abs footer"></div>
<div class="abs" style="left:114px;top:3376px;font-family:'Montserrat',sans-serif;font-weight:700;font-size:17px;color:var(--white);letter-spacing:2px">TORVEN<br>RENEWABLES</div>
<div class="abs foot-title" style="left:390px;top:3290px">Quick Links</div>
<ul class="abs links" style="left:390px;top:3336px">
  <li style="font-weight:500">Home</li><li>About us</li><li>Our Services</li><li>Renewable Solutions</li><li>Contact us</li>
</ul>
<div class="abs foot-title" style="left:633px;top:3288px">Quick Contact</div>
<svg class="abs" style="left:606px;top:3340px" width="14" height="16" viewBox="0 0 14 16"><path d="M7 15 C2 9 2 7 2 6 A5 5 0 0 1 12 6 C12 7 12 9 7 15 Z" fill="none" stroke="#fff"/><circle cx="7" cy="6" r="2" fill="none" stroke="#fff"/></svg>
<div class="abs foot-txt" style="left:633px;top:3333px">48 Larch Row, Westmere,<br>New York 12345, USA</div>
<svg class="abs" style="left:606px;top:3422px" width="14" height="12" viewBox="0 0 14 12"><rect x="1" y="3" width="12" height="8" rx="2" fill="none" stroke="#fff"/><path d="M3 3 V1 H11 V3" fill="none" stroke="#fff"/></svg>
<div class="abs foot-txt" style="left:633px;top:3414px">00 987 654 3210</div>
<svg class="abs" style="left:606px;top:3451px" width="14" height="11" viewBox="0 0 14 11"><rect x="1" y="1" width="12" height="9" fill="none" stroke="#fff"/><path d="M1 1 L7 6 L13 1" fill="none" stroke="#fff"/></svg>
<div class="abs foot-txt" style="left:633px;top:3442px">info@torvenrenewables.com</div>
<div class="abs foot-title" style="left:898px;top:3290px">Newsletter</div>
<div class="abs" style="left:898px;top:3339px;width:240px;font-family:'Poppins',sans-serif;font-size:12.5px;line-height:16px;color:var(--white)">Lorem Ipsum is simply dummy text and typesetting industry.</div>
<div class="abs" style="left:898px;top:3385px;width:226px;height:36px;border-radius:18px;background:var(--white);font-family:'Poppins',sans-serif;font-style:italic;font-size:12px;color:#555;padding:10px 18px">Your Email Address</div>
<div class="abs btn" style="left:898px;top:3429px;width:226px;height:35px;font-size:12px">SUBSCRIBE</div>

<!-- bottom bar -->
<div class="abs" style="left:75px;top:3587px;font-family:'Poppins',sans-serif;font-size:12.5px;color:#333">Copyright © 2022 <b style="font-weight:500">TORVEN RENEWABLES</b> . All Rights Reserved</div>
<div class="abs social" style="left:981px;background:var(--blue)"></div>
<div class="abs social" style="left:1019px;background:#333"></div>
<div class="abs social" style="left:1056px;background:#333"></div>
<div class="abs social" style="left:1094px;background:#333"></div>

</body>
</html>
```